Game, Voice & Dedicated Server Company Needs a Business Card Design

We need a new business card design, centered around our new logo (PSD provided below).

Designs that we do like:
https://pixelmarsh.net/item/corporate-business-card/5382017?s_rank=43 (needs to be made more eye catching)

Our main areas of business are:
- Dedicated Servers
- Game Servers
- Voice Servers
- Mitigation Security Specialists

Industry/Entity Type

Business

Contact Information for Business Card

On the card: (and anything else you would suggest)
- Staff member name
- Staff member position in company
- Staff member phone number
- Staff member email
- Other / Staff member Skype
- Website link

Colors
9bcb3c
abd036

Requirements
Must have
• Design of Card:
• - Green (same green as the logo)
• - Business / Corporate design
• - Something a little different / abstract that shouts premium

```html
<!DOCTYPE html>
<html lang="en">
<head>
<meta charset="utf-8">
<title>Ridgeway Hosting – Business Card</title>
<link rel="stylesheet" href="https://fonts.googleapis.com/css2?family=Montserrat:wght@300;600;700;800&family=Oswald:wght@500&display=swap">
<style>
  :root {
    --canvas: #d9d9d6;
    --card-black: #1f1d1e;
    --card-navy: #25262f;
    --brand-green: #76b043;
    --light-green: #9bcb3c;
    --white: #ffffff;
    --ink: #1b1c1f;
  }
  * { box-sizing: border-box; margin: 0; padding: 0; }
  html, body {
    width: 1200px; height: 900px; overflow: hidden;
    background: var(--canvas);
  }
  .sheet {
    position: relative; width: 1200px; height: 900px;
  }
  .card {
    position: absolute; left: 250px; width: 700px; height: 400px;
    overflow: hidden;
    box-shadow: 0 6px 18px rgba(0,0,0,.18);
  }
  .brand {
    display: flex; align-items: center;
  }
  .brand-mark {
    flex: none; background: var(--light-green);
  }
  .brand-name {
    font-family: "Montserrat", sans-serif; font-weight: 800;
    color: var(--light-green); letter-spacing: -1px;
    line-height: 1; text-transform: uppercase; white-space: nowrap;
  }
  .brand-name span { display: block; }

  /* Back */
  .card--back { top: 40px; background: var(--card-black); }
  .card--back .brand {
    position: absolute; left: 0; right: 0; top: 100px;
    justify-content: center; gap: 26px;
  }
  .card--back .brand-mark { width: 70px; height: 70px; }
  .card--back .brand-name { font-size: 46px; }

  /* Front */
  .card--front { top: 460px; background: var(--card-navy); }
  .card--front .green-side {
    position: absolute; top: 0; right: 0; bottom: 0; width: 360px;
    background: var(--brand-green);
  }
  .identity {
    position: absolute; top: 72px; right: 402px; text-align: right;
    font-family: "Montserrat", sans-serif;
    padding-right: 18px;
  }
  .identity::after {
    content: ""; position: absolute; right: 0; top: 4px;
    width: 4px; height: 58px; background: var(--white);
  }
  .person-name {
    color: var(--light-green); font-size: 33px; line-height: 1;
    letter-spacing: 0.5px; white-space: nowrap;
  }
  .person-name .first { font-weight: 300; }
  .person-name .last { font-weight: 700; }
  .person-role {
    margin-top: 12px; color: var(--white); font-weight: 300;
    font-size: 15px; letter-spacing: 4px;
  }
  .card--front .brand {
    position: absolute; left: 56px; bottom: 62px; gap: 16px;
  }
  .card--front .brand-mark { width: 44px; height: 44px; }
  .card--front .brand-name { font-size: 32px; }
  .contact-panel {
    position: absolute; left: 322px; top: 190px; width: 378px; height: 170px;
    background: var(--brand-green); border-radius: 18px 0 0 18px;
    list-style: none; padding: 12px 0 0 20px;
  }
  .contact-item {
    display: flex; align-items: center; gap: 24px; height: 38px;
    font-family: "Oswald", sans-serif; font-weight: 500;
    font-size: 23px; color: var(--ink); white-space: nowrap;
  }
  .contact-icon {
    width: 30px; height: 30px; flex: none;
  }
</style>
</head>
<body>
<main class="sheet">

  <section class="card card--back" aria-label="Card back">
    <div class="brand">
      <span class="brand-mark"></span>
      <span class="brand-name"><span>Ridgeway</span><span>Hosting</span></span>
    </div>
  </section>

  <section class="card card--front" aria-label="Card front">
    <div class="green-side"></div>

    <div class="identity">
      <p class="person-name"><span class="first">DANIEL</span> <span class="last">REYES</span></p>
      <p class="person-role">MANAGER</p>
    </div>

    <div class="brand">
      <span class="brand-mark"></span>
      <span class="brand-name"><span>Ridgeway</span><span>Hosting</span></span>
    </div>

    <ul class="contact-panel">
      <li class="contact-item">
        <svg class="contact-icon" viewBox="0 0 30 30" aria-hidden="true">
          <circle cx="15" cy="15" r="15" fill="#fff"/>
          <path d="M10.5 8.5l2.6-.6 1.4 3.4-1.7 1.3a9 9 0 0 0 4.6 4.6l1.3-1.7 3.4 1.4-.6 2.6c-.2.6-.8 1-1.4 1A12 12 0 0 1 9.5 9.9c0-.6.4-1.200 1-1.4z" fill="var(--brand-green)"/>
        </svg>
        303-555-0172
      </li>
      <li class="contact-item">
        <svg class="contact-icon" viewBox="0 0 30 30" aria-hidden="true">
          <circle cx="15" cy="15" r="15" fill="#fff"/>
          <g fill="none" stroke="var(--brand-green)" stroke-width="1.8">
            <circle cx="15" cy="15" r="8"/>
            <ellipse cx="15" cy="15" rx="3.5" ry="8"/>
            <path d="M7 15h16"/>
          </g>
        </svg>
        www.ridgeway-hosting.com
      </li>
      <li class="contact-item">
        <svg class="contact-icon" viewBox="0 0 30 30" aria-hidden="true">
          <circle cx="15" cy="15" r="15" fill="#fff"/>
          <rect x="8" y="10" width="14" height="10" rx="1" fill="var(--brand-green)"/>
          <path d="M8.5 10.8L15 15.8l6.5-5" fill="none" stroke="#fff" stroke-width="1.4"/>
        </svg>
        daniel.reyes@mailbox.com
      </li>
      <li class="contact-item">
        <svg class="contact-icon" viewBox="0 0 30 30" aria-hidden="true">
          <circle cx="15" cy="15" r="15" fill="#fff"/>
          <path d="M8 9.5h14a1 1 0 0 1 1 1v7.5a1 1 0 0 1-1 1h-8l-4 3v-3H8a1 1 0 0 1-1-1v-7.5a1 1 0 0 1 1-1z" fill="var(--brand-green)"/>
        </svg>
        daniel.reyes
      </li>
    </ul>
  </section>

</main>
</body>
</html>
```